Responsive Website Design for New Social Site (Building User Account)

KelvaPost.com is a website that allows people to create preformatted emails to be sent out at a later date. The purpose is to allow people to communicate in the event of an accident or death. The beta site is built but not consumable by the public. It needs a new look before we go live.

I’m speaking specifically about the user account. They are admin tools for creating and publishing communications. They include workflow design, document/message storage, and a dashboard.

I currently have a basic design. Now I’m looking for an inspired design. Something interesting and memorable. Something that draws people in. I have a PPT that can provide guidance on what elements need to be on each page but I’m looking for someone who knows how to create engaging websites.

SCOPE OF EFFORT
There are approximately 23 pages to the website but only 5 distinct page appearances
• Dashboard
• Workflow
• Document/Message/Contact Management
• Education Search
• Account Form
I need a few pop-up designs
• Yes/No/Continue
I need a responsive design (3 sizes)

ARTISTIC QUALITIES
Easy to Use/Understand
New/Inventive/Cool/Memorable
Works with the Logo
Consistent Elements (buttons, text, use of color, etc)

TECHNICAL ASPECTS
I’d like the work provided in a storyboard and individual files for development

PHASES
1. Initial Concept
a. 2-3 Designs Ideas. Just the Dashboard and Workflow in responsive formats
2. Build
a. Create all the pages
b. Provide in storyboard in responsive formats
c. 2 Rounds of Revision
3. Final
a. Provide Storyboard and Files

I'd like to see a portfolio of your responsive web design, especially any user accounts you have created. I've attached three of the initial pages. I'd like to see a concept of what you would produce for at least one of the pages.

Thank you for your interest.

```html
<!DOCTYPE html>
<html lang="en">
<head>
<meta charset="utf-8">
<title>KelvaPost – Dashboard</title>
<link href="https://fonts.googleapis.com/css2?family=Arimo:wght@400;700&family=Lato:wght@400;700&display=swap" rel="stylesheet">
<style>
:root{
  --green:#6db33f;
  --green-dark:#5a9a30;
  --dark:#333333;
  --darker:#2b2b2b;
  --card:#d9d9d9;
  --text:#333333;
  --muted:#666666;
  --line:#3a3a3a;
  --row-line:#f2f2f2;
  --white:#ffffff;
  --bg:#ffffff;
}
*{box-sizing:border-box;margin:0;padding:0}
html,body{width:1080px;height:1200px;overflow:hidden;background:var(--bg)}
body{position:relative;font-family:"Arimo",Arial,sans-serif;color:var(--text)}

.site-header{position:absolute;left:0;top:0;width:1080px;height:60px;background:var(--green)}
.brand{position:absolute;left:83px;top:6px}
.brand-row{display:flex;align-items:center;gap:8px}
.brand-mark{width:30px;height:30px;border-radius:50%;background:#2f7fc1}
.brand-name{font:700 28px/1 "Arimo",Arial,sans-serif;color:#3b86c8}
.brand-tagline{font:400 9px/1 "Arimo",Arial,sans-serif;color:#8a5a2a;margin:3px 0 0 58px}
.auth{position:absolute;left:753px;top:19px;width:131px;height:25px;background:var(--green-dark);border-radius:5px;display:flex;border:1px solid #4e8a28}
.auth a{flex:1;color:var(--white);font:400 14px/23px "Arimo",Arial,sans-serif;text-align:center;text-decoration:none}
.auth a+a{border-left:1px solid #4e8a28}
.user{position:absolute;left:913px;top:16px;display:flex;gap:8px}
.user-name{font:700 13px/1 "Arimo",Arial,sans-serif;color:var(--darker)}
.user-logout{font:400 11px/1 "Arimo",Arial,sans-serif;color:var(--darker);margin-top:2px}

.main-nav{position:absolute;left:0;top:60px;width:1080px;height:49px;background:var(--dark)}
.main-nav a{position:absolute;top:13px;height:24px;transform:translateX(-50%);color:var(--white);font:400 14px/24px "Arimo",Arial,sans-serif;text-decoration:none;white-space:nowrap}
.main-nav a.active{background:#111;border-radius:4px;width:72px;text-align:center}
.nav-shade{position:absolute;left:0;top:109px;width:1080px;height:38px;background:linear-gradient(#ececec,#fff)}

.hero{position:absolute;left:77px;top:144px;width:926px;height:199px;border:1px solid #d0d0d0;border-radius:4px;overflow:hidden;background:#ededed}
.hero-photo{position:absolute;left:0;top:0;width:740px;height:199px;background:linear-gradient(90deg,#6d6a63 0%,#9a8a7a 30%,#b7a796 55%,#c9c9bd 75%,rgba(237,237,237,0) 100%)}
.hero-title{position:absolute;left:700px;top:44px;width:230px;text-align:center;font:700 27px/28px "Arimo",Arial,sans-serif;color:var(--green)}
.hero-title .dark{color:var(--darker)}

.stats{position:absolute;left:77px;top:377px;width:926px;height:71px}
.stats .link{position:absolute;top:35px;height:1px;background:var(--line);width:42px}
.stat{position:absolute;top:0;width:185px;height:71px;color:var(--white);font:700 22px/71px "Arimo",Arial,sans-serif;text-align:center}
.stat.green{background:var(--green)}
.stat.dark{background:var(--dark)}

.section-title{position:absolute;left:77px;width:926px;height:24px;display:flex;align-items:center;gap:14px;font:700 21px/24px "Arimo",Arial,sans-serif;color:var(--darker)}
.section-title::before,.section-title::after{content:"";flex:1;height:1px;background:var(--line)}

.plan-card{position:absolute;width:271px;height:112px;background:var(--card);border-radius:5px;text-align:center}
.plan-icon{position:absolute;left:50%;top:-16px;transform:translateX(-50%);width:54px;height:42px;background:var(--green);border:4px solid var(--white);display:flex;align-items:center;justify-content:center}
.plan-name{position:absolute;left:0;right:0;top:35px;font:700 21px/1 "Arimo",Arial,sans-serif;color:var(--darker)}
.plan-desc{position:absolute;left:4px;right:4px;top:59px;font:400 11.5px/19px "Arimo",Arial,sans-serif;color:var(--muted);white-space:nowrap}

.active-plans{position:absolute;left:77px;top:897px;width:926px;height:231px;background:var(--card);border-radius:5px;overflow:hidden}
.active-plans table{width:926px;border-collapse:collapse;table-layout:fixed}
.active-plans thead tr{background:var(--green);height:32px}
.active-plans th{font:400 13px/1 "Lato",Arial,sans-serif;color:var(--darker);text-align:center}
.active-plans th.col-contact{padding-left:36px}
.active-plans tbody tr{height:31px;background:linear-gradient(var(--row-line),var(--row-line)) no-repeat 38px 100%/850px 1px}
.active-plans tbody tr:last-child{background:none}
.active-plans td{font:400 13px/1 "Lato",Arial,sans-serif;color:var(--darker);text-align:center}
.active-plans td:last-child{padding-left:36px}
.col-status{width:108px}.col-name{width:204px}.col-start{width:128px}.col-end{width:196px}.col-docs{width:134px}.col-contact{width:156px}

.site-footer{position:absolute;left:0;top:1161px;width:1080px;height:39px;background:var(--dark);text-align:center;font:400 12px/39px "Lato",Arial,sans-serif;color:var(--green)}
</style>
</head>
<body>

<header class="site-header">
  <div class="brand">
    <div class="brand-row"><span class="brand-mark"></span><span class="brand-name">KelvaPost</span></div>
    <div class="brand-tagline">The most trusted resource for life management</div>
  </div>
  <nav class="auth"><a href="#">Login</a><a href="#">Signup</a></nav>
  <div class="user">
    <svg width="26" height="24" viewBox="0 0 26 24" aria-hidden="true"><circle cx="13" cy="7" r="6" fill="#3a3a3a"/><path d="M1 24c0-7 5-10 12-10s12 3 12 10z" fill="#3a3a3a"/></svg>
    <div><div class="user-name">Rowan Tate</div><div class="user-logout">Logout</div></div>
  </div>
</header>

<nav class="main-nav">
  <a href="#" class="active" style="left:113px">Home</a>
  <a href="#" style="left:225px">Plans</a>
  <a href="#" style="left:352px">Documents</a>
  <a href="#" style="left:492px">Messages</a>
  <a href="#" style="left:625px">Contacts</a>
  <a href="#" style="left:753px">Learning</a>
  <a href="#" style="left:889px">Community</a>
</nav>
<div class="nav-shade"></div>

<section class="hero">
  <div class="hero-photo" role="img" aria-label="Photo of a smiling multi-generation family gathered together outdoors"></div>
  <h1 class="hero-title">Discover Why<br><span class="dark">KelvaPost</span><br>is Important<br>to You</h1>
</section>

<section class="stats">
  <div class="stat green" style="left:0">4 Plans</div>
  <span class="link" style="left:195px"></span>
  <div class="stat dark" style="left:246px">12 Contacts</div>
  <span class="link" style="left:441px"></span>
  <div class="stat green" style="left:494px">8 Documents</div>
  <span class="link" style="left:689px"></span>
  <div class="stat dark" style="left:741px">12 Messages</div>
</section>

<h2 class="section-title" style="top:476px">Recommended Plans</h2>

<article class="plan-card" style="left:77px;top:544px">
  <div class="plan-icon"><svg width="30" height="26" viewBox="0 0 30 26" aria-hidden="true"><path d="M15 22 5 12a5 5 0 0 1 10-6 5 5 0 0 1 10 6z" fill="#fff"/><path d="M15 22v4" stroke="#fff" stroke-width="1.5"/></svg></div>
  <h3 class="plan-name">Life</h3>
  <p class="plan-desc">Lorem Ipsum is simply dummy text of the<br>printing and typesetting industry. Lorem Ipsum</p>
</article>
<article class="plan-card" style="left:405px;top:544px">
  <div class="plan-icon"><svg width="34" height="24" viewBox="0 0 34 24" aria-hidden="true"><path d="M2 20v-6l3-6h10l3 6v6z" fill="none" stroke="#fff" stroke-width="2"/><path d="M16 20v-6l3-6h10l3 6v6z" fill="none" stroke="#fff" stroke-width="2"/><path d="M17 2l-2 5M19 3l-1 4" stroke="#fff" stroke-width="1.5"/></svg></div>
  <h3 class="plan-name">Accident</h3>
  <p class="plan-desc">Lorem Ipsum is simply dummy text of the<br>printing and typesetting industry. Lorem Ipsum</p>
</article>
<article class="plan-card" style="left:732px;top:544px">
  <div class="plan-icon"><svg width="30" height="24" viewBox="0 0 30 24" aria-hidden="true"><path d="M2 11 15 2l13 9z" fill="#fff"/><rect x="5" y="11" width="20" height="11" fill="#fff"/><rect x="9" y="14" width="4" height="4" fill="#6db33f"/><rect x="17" y="14" width="4" height="4" fill="#6db33f"/></svg></div>
  <h3 class="plan-name">Home</h3>
  <p class="plan-desc">Lorem Ipsum is simply dummy text of the<br>printing and typesetting industry. Lorem Ipsum</p>
</article>

<article class="plan-card" style="left:77px;top:704px">
  <div class="plan-icon"><svg width="38" height="20" viewBox="0 0 38 20" aria-hidden="true"><path d="M2 14v-4l6-1 6-6h10l7 6 5 1v4z" fill="#fff"/><circle cx="10" cy="15" r="3" fill="#6db33f" stroke="#fff" stroke-width="1.5"/><circle cx="28" cy="15" r="3" fill="#6db33f" stroke="#fff" stroke-width="1.5"/></svg></div>
  <h3 class="plan-name">Auto</h3>
  <p class="plan-desc">Lorem Ipsum is simply dummy text of the<br>printing and typesetting industry. Lorem Ipsum</p>
</article>
<article class="plan-card" style="left:405px;top:704px">
  <div class="plan-icon"><svg width="28" height="28" viewBox="0 0 28 28" aria-hidden="true"><circle cx="16" cy="12" r="9" fill="none" stroke="#fff" stroke-width="1.8"/><path d="M7 12h18M16 3c-4 5-4 13 0 18M16 3c4 5 4 13 0 18" fill="none" stroke="#fff" stroke-width="1.5"/><rect x="2" y="17" width="10" height="8" fill="#fff"/></svg></div>
  <h3 class="plan-name">Travel</h3>
  <p class="plan-desc">Lorem Ipsum is simply dummy text of the<br>printing and typesetting industry. Lorem Ipsum</p>
</article>
<article class="plan-card" style="left:732px;top:704px">
  <div class="plan-icon"><svg width="28" height="28" viewBox="0 0 28 28" aria-hidden="true"><circle cx="14" cy="14" r="11" fill="none" stroke="#fff" stroke-width="2"/><path d="M14 8v12M8 14h12" stroke="#fff" stroke-width="2"/></svg></div>
  <h3 class="plan-name">More</h3>
  <p class="plan-desc">Lorem Ipsum is simply dummy text of the<br>printing and typesetting industry. Lorem Ipsum</p>
</article>

<h2 class="section-title" style="top:845px">Active Plans</h2>

<section class="active-plans">
  <table>
    <thead>
      <tr><th class="col-status">Status</th><th class="col-name">Plan Name</th><th class="col-start">Start Date</th><th class="col-end">End Date</th><th class="col-docs">Documents</th><th class="col-contact">Contact</th></tr>
    </thead>
    <tbody>
      <tr><td>Start</td><td>Lorem ipsum dollar</td><td>10/5/2015</td><td>18/8/2015</td><td>2</td><td>3</td></tr>
      <tr><td>Start</td><td>Lorem ipsum dollar</td><td>10/5/2015</td><td>18/8/2015</td><td>2</td><td>3</td></tr>
      <tr><td>Start</td><td>Lorem ipsum dollar</td><td>10/5/2015</td><td>18/8/2015</td><td>2</td><td>3</td></tr>
      <tr><td>Start</td><td>Lorem ipsum dollar</td><td>10/5/2015</td><td>18/8/2015</td><td>2</td><td>3</td></tr>
      <tr><td>Start</td><td>Lorem ipsum dollar</td><td>10/5/2015</td><td>18/8/2015</td><td>2</td><td>3</td></tr>
      <tr><td>Start</td><td>Lorem ipsum dollar</td><td>10/5/2015</td><td>18/8/2015</td><td>2</td><td>3</td></tr>
    </tbody>
  </table>
</section>

<footer class="site-footer">Copyright © 2015 KelvaPost. All Rights Reserved.</footer>

</body>
</html>
```